Fancy looking Inspection Postcard

Postcard needed for customers to inspect their product once it is delivered. We'll be giving them the steps for inspecting their product and to contact us if any issues arise. Would like to see something that sticks out but uses our company's colors. Would like to see creativity. Possibly utilizing the diamond steel background like we have in our logo.

Target Market(s)

Customers of our manufacturing shop

Industry/Entity Type

Manufacturing - metal wall art, custom products

Requirements
Must have
• our colors and logo
Nice to have
• get creative. i like creativity

```html
<!DOCTYPE html>
<html lang="en">
<head>
<meta charset="utf-8">
<title>Inspection Postcard – Ridge Creek Fabrication</title>
<link rel="stylesheet" href="https://fonts.googleapis.com/css2?family=Poppins:wght@600;700&family=Teko:wght@500;600&display=swap">
<style>
  :root {
    --yellow: #f4e800;
    --yellow-deep: #e2d200;
    --green: #6aa33a;
    --ink: #141414;
    --panel: #1c1c1c;
    --page: #e8e7e4;
  }
  * { margin: 0; padding: 0; box-sizing: border-box; }
  html, body { width: 1200px; height: 1092px; overflow: hidden; background: var(--page); }
  body { position: relative; font-family: "Poppins", sans-serif; }

  .postcard {
    position: absolute; width: 760px; height: 507px; overflow: hidden;
    background: var(--panel);
    box-shadow: 0 6px 18px rgba(0,0,0,.25);
  }
  .postcard--feedback { left: 60px; top: 30px; }
  .postcard--steps { left: 380px; top: 555px; }
  .postcard svg.shapes { position: absolute; inset: 0; }

  /* feedback side */
  .feedback-photo { position: absolute; inset: 0; background: linear-gradient(120deg, #2b2b2b 0%, #1e1e1e 55%, #121212 100%); }
  .feedback-text { position: absolute; left: 0; top: 0; width: 270px; text-align: center; color: var(--yellow); font-weight: 700; }
  .feedback-text .ask { position: absolute; left: 16px; width: 240px; top: 74px; font-size: 19px; color: var(--green); font-weight: 600; }
  .feedback-text .review { position: absolute; left: 24px; width: 224px; top: 118px; font-size: 12.5px; line-height: 17px; }
  .feedback-text .problem { position: absolute; left: 10px; width: 252px; top: 170px; font-size: 14.5px; line-height: 20px; }
  .feedback-text .problem span { color: var(--green); font-size: 14px; }
  .feedback-text .call { position: absolute; left: 16px; width: 240px; top: 232px; font-size: 14.5px; }
  .feedback-text .phone { position: absolute; left: 16px; width: 240px; top: 254px; font-family: "Teko", sans-serif; font-size: 42px; color: var(--green); font-weight: 600; line-height: 42px; }
  .contact-list { position: absolute; left: 16px; top: 325px; width: 220px; font-size: 10.5px; color: var(--yellow); font-weight: 700; text-align: left; }
  .contact-list p { margin-bottom: 20px; line-height: 14px; white-space: nowrap; }
  .contact-list .value { color: var(--green); }
  .contact-list .num { font-family: "Teko", sans-serif; font-size: 20px; font-weight: 500; color: var(--yellow); }

  /* steps side */
  .step { position: absolute; }
  .step-tab {
    position: absolute; width: 60px; height: 34px; border: 1.5px solid #4b5a2a; border-radius: 8px 8px 0 0;
    background: #1a1a1a;
  }
  .step-tab .label { position: absolute; left: 3px; top: 27px; transform: rotate(-90deg); transform-origin: 0 0; font-size: 7px; color: var(--green); font-weight: 700; letter-spacing: .5px; }
  .step-tab .num { position: absolute; left: 15px; top: -2px; font-family: "Teko", sans-serif; font-size: 26px; color: var(--green); font-weight: 600; }
  .step-box {
    position: absolute; border-radius: 10px;
    background: linear-gradient(90deg, var(--yellow-deep), var(--yellow));
    padding: 10px 0 0 38px;
  }
  .step-box h3 { font-size: 16px; color: var(--green); font-weight: 600; line-height: 20px; }
  .step-box ul { list-style: none; margin-top: 2px; }
  .step-box li { font-size: 11px; color: var(--ink); font-weight: 600; line-height: 16px; padding-left: 4px; }
  .step-box li::before { content: "• "; }

  .brand-mark { position: absolute; left: 402px; top: 72px; width: 136px; height: 136px; border-radius: 50%; background: var(--ink); }
  .brand-name { position: absolute; left: 402px; top: 118px; width: 136px; text-align: center; font-family: "Teko", sans-serif; font-weight: 600; font-size: 24px; line-height: 22px; color: var(--green); }

  .footer-line { position: absolute; left: 0; top: 470px; width: 620px; text-align: center; font-size: 15px; font-weight: 600; color: var(--green); line-height: 20px; }
</style>
</head>
<body>

<section class="postcard postcard--feedback">
  <div class="feedback-photo" role="img" aria-label="Darkened photo of a metalworker cutting decorative steel wall art on a workbench"></div>
  <svg class="shapes" width="760" height="507" viewBox="0 0 760 507" aria-hidden="true">
    <path d="M0,20 L54,4 Q160,46 292,8 C298,240 284,420 180,507 L0,507 Z" fill="var(--yellow)"/>
    <path d="M0,40 L54,24 Q160,64 272,34 C280,260 262,420 155,507 L0,507 Z" fill="#1b1a1a" stroke="#000" stroke-width="2"/>
  </svg>
  <div class="feedback-text">
    <p class="ask">Did we do a good job?</p>
    <p class="review">If you think so, leave us a review on ReviewHub?</p>
    <p class="problem">If not, Please let us know –<br><span>info@ridgefab.com</span></p>
    <p class="call">or call us</p>
    <p class="phone">08-555-0142</p>
    <div class="contact-list">
      <p>Email us at: <span class="value">orders@ridgefab.com</span></p>
      <p>shoot us a text <span class="num">-208-555-0187</span></p>
      <p>or reach out via<br><span class="value">www.ridgefab.com/contact</span></p>
    </div>
  </div>
</section>

<section class="postcard postcard--steps">
  <svg class="shapes" width="760" height="507" viewBox="0 0 760 507" role="img" aria-label="Photo of a welder in protective gear with bright blue sparks">
    <defs>
      <radialGradient id="welderGlow" cx="0.8" cy="0.75" r="0.8">
        <stop offset="0" stop-color="#cfe3ff"/>
        <stop offset="0.25" stop-color="#4d7db4"/>
        <stop offset="1" stop-color="#0f1d2e"/>
      </radialGradient>
    </defs>
    <path d="M466,2 L710,2 L760,18 L760,507 L660,507 C566,420 500,250 466,2 Z" fill="var(--yellow)"/>
    <path d="M490,42 L704,30 L760,46 L760,507 L690,507 C596,420 522,262 490,42 Z" fill="url(#welderGlow)" stroke="#000" stroke-width="2"/>
    <polygon points="0,468 612,468 646,490 0,490" fill="var(--yellow)"/>
  </svg>

  <div class="brand-mark"></div>
  <p class="brand-name">RIDGE CREEK<br>FABRICATION</p>

  <div class="step" style="left:28px;top:40px">
    <div class="step-tab"><span class="label">STEP</span><span class="num">1.</span></div>
    <div class="step-box" style="left:38px;top:8px;width:292px;height:70px">
      <h3>Inspect general shape</h3>
      <ul><li>Is it what you expected?</li><li>Is it bent, disoriented?</li></ul>
    </div>
  </div>

  <div class="step" style="left:28px;top:150px">
    <div class="step-tab"><span class="label">STEP</span><span class="num">2.</span></div>
    <div class="step-box" style="left:38px;top:8px;width:334px;height:70px">
      <h3>Inspect the welds if there are any</h3>
      <ul><li>Do they look clean?</li><li>Are there any gaps?</li></ul>
    </div>
  </div>

  <div class="step" style="left:28px;top:261px">
    <div class="step-tab"><span class="label">STEP</span><span class="num">3.</span></div>
    <div class="step-box" style="left:38px;top:8px;width:292px;height:70px">
      <h3>Inspect the finish</h3>
      <ul><li>Are there any areas not finished?</li><li>Are the colors what you expected?</li></ul>
    </div>
  </div>

  <div class="step" style="left:28px;top:372px">
    <div class="step-tab"><span class="label">STEP</span><span class="num">4.</span></div>
    <div class="step-box" style="left:38px;top:8px;width:292px;height:70px">
      <h3>Check for functionality</h3>
      <ul><li>Does it work the way you want it to</li><li>Is it what you expected?</li></ul>
    </div>
  </div>

  <p class="footer-line">(208) 555-0187 | WWW.RIDGEFAB.COM</p>
</section>

</body>
</html>
```